TrellisCover Mobile App needs a new skin

We need to add some sparkle to our mobile application. The app is already built with some of the functionality, screens and components (vanilla material design) and now it needs some styling and inspiration. The application simplifies insurance form capturing and communication to/from the broker. Further to that it has some value added services.

Industry/Entity Type

Insurance Broker

Font styles to use
Sans Serif

Requirements
Must have
• Modern, friendly styling and colors. Material design principles.
Nice to have
• Thinking of a themed background photo with the form elements in a more glassy / semi transparent style.
• Would like to use the same app for some customers as a white labeled version, then just change the themed background image, logo and select dark or light theme for them.

```html
<!DOCTYPE html>
<html lang="en">
<head>
<meta charset="utf-8">
<title>TrellisCover app screens</title>
<link rel="stylesheet" href="https://fonts.googleapis.com/css2?family=Didact+Gothic&family=Montserrat:wght@500;600&display=swap">
<style>
:root{
  --backdrop:#141617;
  --teal:#86cfc3;
  --green:#86cfa0;
  --tabbar:#3b5a58;
  --tab-active:#86cfc3;
  --card:#f4f4f4;
  --ink:#1f2424;
  --ink-soft:#3c4242;
  --rule:#d6d8d8;
  --link:#5bbfc9;
  --alert:#d9717a;
  --white:#ffffff;
}
*{box-sizing:border-box;margin:0;padding:0}
html,body{width:1200px;height:1200px;overflow:hidden;background:var(--backdrop)}
body{position:relative;font-family:"Didact Gothic",sans-serif;color:var(--ink)}
.screen{position:absolute;top:275px;width:366px;height:650px;background:var(--white);overflow:hidden}
.screen--home{left:27px}
.screen--profile{left:417px}
.screen--claims{left:807px}

.status{position:absolute;top:0;left:0;right:0;height:22px;background:var(--teal);color:var(--white);font-family:"Montserrat",sans-serif;font-size:10px;display:flex;align-items:center;justify-content:space-between;padding:0 6px}
.status__battery{display:inline-block;width:18px;height:8px;border:1px solid var(--white);margin-left:3px;vertical-align:middle;position:relative}
.status__battery::after{content:"";position:absolute;left:1px;top:1px;width:10px;height:4px;background:var(--white)}
.appbar{position:absolute;top:22px;left:0;right:0;height:47px;background:var(--teal);color:var(--white);display:flex;align-items:center;justify-content:center;font-family:"Montserrat",sans-serif;font-weight:500;font-size:14.5px;letter-spacing:.3px}
.appbar__bell{position:absolute;right:14px;top:13px}
.appbar__back{position:absolute;left:16px;top:15px}
.appbar__save{position:absolute;right:15px;font-size:13.5px}

.card{position:absolute;left:15px;width:335px;background:var(--card)}
.card__title{font-family:"Montserrat",sans-serif;font-weight:600;font-size:14.5px;padding:10px 15px 6px}
.card__text{font-size:13px;line-height:16px;padding:0 15px;color:var(--ink-soft)}
.card__action{position:absolute;left:0;right:0;bottom:0;height:30px;background:var(--green);color:var(--white);font-family:"Montserrat",sans-serif;font-weight:500;font-size:13.5px;display:flex;align-items:center;justify-content:center;letter-spacing:.3px}

.messages{position:absolute;left:0;right:0;top:352px}
.messages__title{font-family:"Montserrat",sans-serif;font-weight:600;font-size:14.5px;padding-left:15px;margin-bottom:10px}
.message{margin:0 17px 0 41px;padding:4px 0 14px;border-bottom:1px solid var(--rule);margin-bottom:10px}
.message__head{display:flex;justify-content:space-between;font-family:"Montserrat",sans-serif;font-weight:600;font-size:11px;margin-bottom:6px}
.message__time{font-family:"Didact Gothic",sans-serif;font-weight:400;color:#8a8f8f;font-size:10.5px}
.message__body{font-size:13px;line-height:16px}
.message__link{font-size:12.5px;color:var(--link)}
.message:first-of-type{margin-left:41px}
.message--shift{margin-left:42px}

.field{position:absolute;left:17px;right:17px;height:79px;border-bottom:1px solid var(--rule)}
.field__label{position:absolute;left:25px;top:8px;font-family:"Montserrat",sans-serif;font-weight:600;font-size:14.5px}
.field__value{position:absolute;left:35px;top:45px;font-size:13px;color:var(--ink-soft);letter-spacing:.4px}
.screen--claims .field__label{left:0}
.screen--claims .field__value{left:18px}
.field__pin{position:absolute;right:16px;top:44px}

.address{position:absolute;left:15px;top:435px;width:336px;height:110px;background:var(--card);padding:14px 29px;font-size:13px;line-height:16px;color:var(--ink-soft)}
.signout{position:absolute;right:25px;top:563px;color:var(--alert);font-family:"Montserrat",sans-serif;font-weight:600;font-size:13px;letter-spacing:.5px}

.tabbar{position:absolute;left:0;right:0;bottom:0;height:52px;background:var(--tabbar);display:flex}
.tab{flex:1;display:flex;flex-direction:column;align-items:center;justify-content:center;color:var(--white);font-size:12px;gap:2px}
.tab svg{width:24px;height:24px;stroke:currentColor;fill:none;stroke-width:2}
.tab--active{color:var(--tab-active)}
</style>
</head>
<body>

<!-- Home -->
<section class="screen screen--home">
  <div class="status"><span>●●●●● Carrier</span><span>9:23 AM</span><span>66%<span class="status__battery"></span></span></div>
  <header class="appbar">HOME
    <svg class="appbar__bell" width="18" height="20" viewBox="0 0 18 20"><path d="M9 2a5 5 0 0 0-5 5v5l-2 3h14l-2-3V7a5 5 0 0 0-5-5z" fill="#fff"/><circle cx="9" cy="17.5" r="2" fill="#fff"/><circle cx="15" cy="2.5" r="2.2" fill="#e06a6a"/></svg>
  </header>
  <div class="card" style="top:87px;height:113px">
    <h2 class="card__title">Emergency</h2>
    <p class="card__text">Send S.O.S notification to your energency center and they will call back in seconds.</p>
    <div class="card__action">SEND S.O.S</div>
  </div>
  <div class="card" style="top:217px;height:112px">
    <h2 class="card__title" style="padding-left:17px">Road Side Assistance</h2>
    <p class="card__text">24 Hour assistance for any breakdown or towing assistance.</p>
    <div class="card__action">REQUEST ASSISTANCE</div>
  </div>
  <div class="messages">
    <h2 class="messages__title">Message</h2>
    <div class="message" style="margin-left:41px">
      <div class="message__head"><span>BROKER</span><span class="message__time">01h</span></div>
      <p class="message__body">Your claim was registered this morning.</p>
      <p class="message__link">https://files.claimdesk.example/up....</p>
    </div>
    <div class="message message--shift">
      <div class="message__head"><span>INSURER</span><span class="message__time">01h</span></div>
      <p class="message__body">Your claim was paid into your account. and we will notify you once next due.</p>
      <p class="message__link">http://www.payoutnotes.example/get-paid....</p>
    </div>
    <div class="message message--shift" style="border:0">
      <div class="message__head"><span>BROKER</span><span class="message__time">01h</span></div>
      <p class="message__body">Your claim was registered this morning.</p>
    </div>
  </div>
  <nav class="tabbar">
    <div class="tab tab--active"><svg viewBox="0 0 24 24"><path d="M3 9l9-5 9 5zM5 10v8M9.5 10v8M14.5 10v8M19 10v8M3 21h18"/></svg>Home</div>
    <div class="tab"><svg viewBox="0 0 24 24"><path d="M12 2l8 3v6c0 5-3.5 9-8 11-4.5-2-8-6-8-11V5z"/><circle cx="12" cy="10" r="2"/><path d="M8.5 16a3.5 3.5 0 0 1 7 0"/></svg>Insure</div>
    <div class="tab"><svg viewBox="0 0 24 24"><path d="M9 3h6v8h-6zM6 11h12v6H6zM4 21h16"/></svg>Claim</div>
    <div class="tab"><svg viewBox="0 0 24 24"><circle cx="12" cy="7" r="4"/><path d="M4 22v-3a6 6 0 0 1 6-6h4a6 6 0 0 1 6 6v3z"/></svg>Profile</div>
  </nav>
</section>

<!-- Edit profile -->
<section class="screen screen--profile">
  <div class="status"><span>●●●●● Carrier</span><span>9:23 AM</span><span>66%<span class="status__battery"></span></span></div>
  <header class="appbar">
    <svg class="appbar__back" width="10" height="18" viewBox="0 0 10 18"><path d="M9 1L1 9l8 8" stroke="#fff" stroke-width="1.6" fill="none"/></svg>
    EDIT PROFILE<span class="appbar__save">Save</span>
  </header>
  <div class="field" style="top:83px"><span class="field__label">First Name</span><span class="field__value" style="left:27px">DANI</span></div>
  <div class="field" style="top:162px"><span class="field__label">Last Name</span><span class="field__value" style="left:27px">MERWE</span></div>
  <div class="field" style="top:241px"><span class="field__label">Email</span><span class="field__value" style="left:27px">dani.merwe@mailbox.example</span></div>
  <div class="field" style="top:321px"><span class="field__label">Telephone</span><span class="field__value" style="left:27px">09876543210</span></div>
  <div class="field" style="top:400px;border:0;height:30px"><span class="field__label" style="left:26px">Address</span></div>
  <div class="address">14 NW&nbsp; Kestrel rd,<br>Langbaai<br>WC<br>7402</div>
  <div class="signout">SIGN OUT</div>
  <nav class="tabbar">
    <div class="tab"><svg viewBox="0 0 24 24"><path d="M3 9l9-5 9 5zM5 10v8M9.5 10v8M14.5 10v8M19 10v8M3 21h18"/></svg>Home</div>
    <div class="tab"><svg viewBox="0 0 24 24"><path d="M12 2l8 3v6c0 5-3.5 9-8 11-4.5-2-8-6-8-11V5z"/><circle cx="12" cy="10" r="2"/><path d="M8.5 16a3.5 3.5 0 0 1 7 0"/></svg>Insure</div>
    <div class="tab"><svg viewBox="0 0 24 24"><path d="M9 3h6v8h-6zM6 11h12v6H6zM4 21h16"/></svg>Claim</div>
    <div class="tab tab--active"><svg viewBox="0 0 24 24"><circle cx="12" cy="7" r="4"/><path d="M4 22v-3a6 6 0 0 1 6-6h4a6 6 0 0 1 6 6v3z"/></svg>Profile</div>
  </nav>
</section>

<!-- Claims -->
<section class="screen screen--claims">
  <div class="status"><span>●●●●● Carrier</span><span>9:23 AM</span><span>66%<span class="status__battery"></span></span></div>
  <header class="appbar">CLAIMS
    <svg class="appbar__bell" width="18" height="20" viewBox="0 0 18 20"><path d="M9 2a5 5 0 0 0-5 5v5l-2 3h14l-2-3V7a5 5 0 0 0-5-5z" fill="#fff"/><circle cx="9" cy="17.5" r="2" fill="#fff"/><circle cx="15" cy="2.5" r="2.2" fill="#e06a6a"/></svg>
  </header>
  <div class="card" style="top:87px;height:136px">
    <h2 class="card__title">Please Note</h2>
    <p class="card__text">This Claim from should be used as soon as possilbe after the mishap. Dates and locations are tracked automatically from your device where possible</p>
    <div class="card__action">DISMISS</div>
  </div>
  <div class="field" style="top:237px;left:18px;right:17px"><span class="field__label">Policy Number</span><span class="field__value">ARU39857458</span></div>
  <div class="field" style="top:316px;left:18px;right:17px"><span class="field__label">Date of loss</span><span class="field__value">2016 – 08 – 16</span></div>
  <div class="field" style="top:396px;left:18px;right:17px"><span class="field__label">Time of loss</span><span class="field__value">06 :09 pm</span></div>
  <div class="field" style="top:475px;left:18px;right:17px"><span class="field__label">Place of loss</span><span class="field__value">2200 Harbor Ave, Bayview, CA, 28338</span>
    <svg class="field__pin" width="11" height="16" viewBox="0 0 11 16"><path d="M5.5 0A5.5 5.5 0 0 0 0 5.5C0 9.5 5.5 16 5.5 16S11 9.5 11 5.5A5.5 5.5 0 0 0 5.5 0z" fill="#111"/><circle cx="5.5" cy="5.5" r="2" fill="#fff"/></svg>
  </div>
  <nav class="tabbar">
    <div class="tab"><svg viewBox="0 0 24 24"><path d="M3 9l9-5 9 5zM5 10v8M9.5 10v8M14.5 10v8M19 10v8M3 21h18"/></svg>Home</div>
    <div class="tab"><svg viewBox="0 0 24 24"><path d="M12 2l8 3v6c0 5-3.5 9-8 11-4.5-2-8-6-8-11V5z"/><circle cx="12" cy="10" r="2"/><path d="M8.5 16a3.5 3.5 0 0 1 7 0"/></svg>Insure</div>
    <div class="tab"><svg viewBox="0 0 24 24"><path d="M9 3h6v8h-6zM6 11h12v6H6zM4 21h16"/></svg>Claim</div>
    <div class="tab tab--active"><svg viewBox="0 0 24 24"><circle cx="12" cy="7" r="4"/><path d="M4 22v-3a6 6 0 0 1 6-6h4a6 6 0 0 1 6 6v3z"/></svg>Profile</div>
  </nav>
</section>

</body>
</html>
```